Adjust children's activity materials to branding and theme

Hello, we are a global kindergarten (nursery) chain and would like to provide branded printable activity sheets for our schools around the world, that would also reflect the theme of the curriculum.
We can provide the activity sheets that then need to be converted to our style and branded with our logo, colours and branding elements and include an item that reflects the theme, in our visual style. A full branding and colour codes guide is available for the chosen artist.

The 'grapheme' booklet attachment is provided as an example, please let us know how many similar pages you would be able to process within the budget. Each page is a standalone design task and can be printed out individually or as a booklet.

Industry/Entity Type

Early Education

Requirements
Must have
• BrightNest branding

```html
<!DOCTYPE html>
<html lang="en">
<head>
<meta charset="UTF-8">
<title>Graphics Notebook – BrightNest</title>
<link rel="stylesheet" href="https://fonts.googleapis.com/css2?family=League+Spartan:wght@600;800&display=swap">
<style>
  :root {
    --page-bg: #ebe9e4;
    --paper: #ffffff;
    --teal: #6ea3a8;
    --coral: #ec705b;
    --rose: #d49aaa;
    --sun: #f7c100;
    --ink: #111111;
    --skin: #f7c29a;
  }
  * { margin: 0; padding: 0; box-sizing: border-box; }
  html, body {
    width: 1200px;
    height: 1000px;
    overflow: hidden;
    background: var(--page-bg);
  }
  .cover {
    position: absolute;
    left: 309px;
    top: 78px;
    width: 596px;
    height: 842px;
    background: var(--paper);
    overflow: hidden;
    font-family: "League Spartan", "Futura", sans-serif;
  }
  .cover-art {
    position: absolute;
    inset: 0;
    width: 596px;
    height: 842px;
  }
  .title {
    position: absolute;
    top: 80px;
    left: 0;
    width: 100%;
    text-align: center;
    color: var(--paper);
    font-weight: 800;
    font-size: 74px;
    line-height: 80px;
    letter-spacing: 3px;
    text-shadow: 5px 5px 0 var(--coral);
  }
  .age-badge {
    position: absolute;
    left: 500px;
    top: 32px;
    width: 66px;
    height: 66px;
    border: 2.5px solid var(--paper);
    border-radius: 50%;
    color: var(--paper);
    font-weight: 800;
    font-size: 14px;
    line-height: 15px;
    text-align: center;
    display: flex;
    flex-direction: column;
    justify-content: center;
    padding-top: 3px;
  }
  .tagline {
    position: absolute;
    top: 319px;
    left: 0;
    width: 100%;
    text-align: center;
    color: var(--ink);
    font-weight: 800;
    font-size: 19px;
    letter-spacing: 0.6px;
  }
  .child-illustration {
    position: absolute;
    left: 195px;
    top: 388px;
    width: 345px;
    height: 340px;
    border-radius: 48% 48% 30% 30%;
    background: linear-gradient(180deg, #f3d3b8 0%, #f2a48f 55%, #ec8470 100%);
    opacity: 0.85;
  }
  .footer-band {
    position: absolute;
    left: 0;
    bottom: 0;
    width: 100%;
    height: 80px;
    background: var(--teal);
    display: flex;
    align-items: center;
    justify-content: center;
  }
  .brand-name {
    color: var(--paper);
    font-weight: 600;
    font-size: 31px;
    letter-spacing: 0.3px;
    padding-top: 4px;
  }
</style>
</head>
<body>
  <main class="cover">
    <svg class="cover-art" viewBox="0 0 596 842" aria-hidden="true">
      <path class="header-arc" d="M0 0 H596 V152 A355 355 0 0 1 0 152 Z" fill="var(--teal)"/>
      <rect class="trace-square" x="62" y="366" width="128" height="128"
            fill="none" stroke="var(--rose)" stroke-width="8" stroke-dasharray="20 11"/>
      <polyline class="trace-zigzag" points="9,594 71,577 91,664 181,640 201,734"
                fill="none" stroke="var(--coral)" stroke-width="8" stroke-dasharray="20 11"/>
      <circle class="trace-circle" cx="591" cy="634" r="97"
              fill="none" stroke="var(--sun)" stroke-width="8" stroke-dasharray="17 10"/>
    </svg>

    <h1 class="title">GRAPHICS<br>NOTEBOOK</h1>
    <div class="age-badge"><span>3-6</span><span>AGES</span></div>
    <p class="tagline">First step towards writing</p>

    <div class="child-illustration" role="img"
         aria-label="Illustration of a smiling child in a coral dress tracing a dashed square with a pencil"></div>

    <footer class="footer-band">
      <span class="brand-name">BrightNest</span>
    </footer>
  </main>
</body>
</html>
```